Digital Agency Needs a Relaunch

We are looking for a modern, top-notch design to elevate our brand to win new clients. It has to build on the clarity of message in the current wireframes and must fit together well on Wordpress.

The winning designer will need to complete the other pages, but please focus on the homepage as the base of your proposed designs for us.

Use the existing logo as a point, and the colour scheme should be around that, we currently use these colours, but you can suggest new mixes:
Purple: #5c306b
Orange: #e27927
Grey: #5f4f61
Light grey: #cacaca
Off white: #ececec
Blue: #674ea7
Updates

Target Market(s)

Decent Sized SME Businesses (20+ Staff, Over £1m turnover)

Industry/Entity Type

Digital Marketing

Number of Pages Required

5+ page

Font styles to use
Sans Serif

Colors

Designer to choose colors to be used in the design.

Requirements
Must have
• A real attention on the design piece. Ignore the current website and really focus on the messaging and the brief.
Nice to have
• Read the messages and think about the impact. Use the purple in the logo more than the orange, but try to keep it smart rather than cool
Should not have
• Inconsistent design, serif fonts, stock images and not meeting the wireframes.

```html
<!DOCTYPE html>
<html lang="en">
<head>
<meta charset="utf-8">
<title>Vanta Digital — Growth works for you</title>
<link rel="stylesheet" href="https://fonts.googleapis.com/css2?family=Poppins:wght@400;500;600;700&family=Open+Sans:wght@400;600&display=swap">
<style>
:root{
  --orange:#f0641f;
  --orange-2:#f7941d;
  --ink:#222222;
  --text:#555555;
  --topbar:#2a2a2a;
  --hero-bg:#f2f2f2;
  --section-bg:#f4f6f8;
  --navy:#1f2c4c;
  --navy-deep:#16213d;
  --cta-grey:#9b9b9b;
  --white:#ffffff;
  --line:#e3e3e3;
}
*{box-sizing:border-box;margin:0;padding:0}
html,body{width:1200px;height:3286px;overflow:hidden}
body{font-family:"Open Sans",sans-serif;color:var(--text);background:var(--white);position:relative}
h1,h2,h3,h4,.btn,.nav a,.logo{font-family:"Poppins",sans-serif}
a{color:inherit;text-decoration:none}

/* top bar */
.topbar{position:absolute;left:0;top:0;width:1200px;height:40px;background:var(--topbar)}
.social{display:flex;gap:10px}
.social span{width:23px;height:23px;border:1px solid #888;border-radius:50%;display:block}
.topbar .social{position:absolute;left:96px;top:8px}
.toplinks{position:absolute;right:96px;top:12px;display:flex;gap:32px;font-size:11px;color:#eee}

/* header */
.header{position:absolute;top:40px;left:0;width:1200px;height:77px;background:var(--white)}
.logo{position:absolute;left:100px;top:14px;color:var(--orange);font-weight:500;font-size:28px;line-height:1}
.logo small{display:block;font-size:9px;letter-spacing:4px;color:#888;margin-top:2px;padding-left:22px}
.nav{position:absolute;left:357px;top:30px;display:flex;gap:36px;font-size:13px;color:#333}
.search{position:absolute;left:888px;top:27px;width:26px;height:26px;border-radius:50%;background:#ddd}
.btn{display:inline-flex;align-items:center;justify-content:center;gap:14px;color:var(--white);background:linear-gradient(90deg,var(--orange),var(--orange-2));border-radius:30px;font-weight:500;font-size:13px}
.header .btn{position:absolute;left:938px;top:15px;width:165px;height:47px}

/* hero */
.hero{position:absolute;top:117px;left:0;width:1200px;height:648px;background:var(--hero-bg);overflow:hidden}
.hero-badge{position:absolute;left:96px;top:156px;width:64px;height:64px;border-radius:50%;background:var(--white);border:3px solid var(--orange)}
.hero-tags{position:absolute;left:185px;top:174px;color:var(--orange);font-family:"Poppins",sans-serif;font-weight:600;font-size:16px;word-spacing:2px}
.hero h1{position:absolute;left:96px;top:235px;font-size:47px;line-height:60px;color:var(--ink);font-weight:700}
.hero p{position:absolute;left:96px;top:368px;width:420px;font-size:12.5px;line-height:19px}
.hero .btn{position:absolute;left:96px;top:442px;width:172px;height:47px}
.hero-art{position:absolute;left:612px;top:0;width:528px;height:505px;border-radius:0 0 46% 46%/0 0 38% 38%;background:linear-gradient(160deg,#fbe3c8 0%,#e4e6ef 35%,#c9d0ea 65%,#f6a24a 100%)}
.deco{position:absolute;border-radius:50%}

/* intro */
.intro{position:absolute;top:765px;left:0;width:1200px;height:602px;background:var(--white)}
.intro-art-a{position:absolute;left:96px;top:117px;width:210px;height:320px;border:1px solid #ccc;background:linear-gradient(160deg,#f5f7fb,#f3c2bb 70%,#e9594a)}
.intro-art-b{position:absolute;left:328px;top:207px;width:210px;height:316px;border:1px solid #ccc;background:linear-gradient(160deg,#f4f1f8,#d49be3 65%,#a65bc4)}
.intro-pill{position:absolute;left:188px;top:144px;width:305px;height:45px;border-radius:25px;background:var(--orange);color:var(--white);font-family:"Poppins",sans-serif;font-weight:500;font-size:17px;display:flex;align-items:center;justify-content:center;box-shadow:0 0 0 4px #fff}
.intro-lines{position:absolute;left:96px;top:460px;width:210px;height:8px;border-top:2px solid #9bb0e0;border-bottom:2px solid #9bb0e0}
.intro h2{position:absolute;left:612px;top:132px;width:500px;font-size:31px;line-height:41px;color:var(--ink);font-weight:600}
.checks{position:absolute;left:612px;top:252px;width:490px;list-style:none;font-size:12px;line-height:16px}
.checks li{position:relative;padding-left:19px;margin-bottom:8px}
.checks li svg{position:absolute;left:0;top:3px}
.intro h3{position:absolute;left:612px;top:420px;font-size:19px;color:var(--ink);font-weight:600}
.intro .btn{position:absolute;left:612px;top:459px;width:141px;height:46px;font-size:14px;font-weight:400;background:var(--orange)}
.intro-watermark{position:absolute;left:1024px;top:318px;width:164px;height:152px;border:10px solid #f0f0f0;border-radius:10px}

/* services */
.services{position:absolute;top:1367px;left:0;width:1200px;height:650px;background:var(--section-bg)}
.section-title{position:absolute;left:0;width:1200px;text-align:center;font-size:31px;font-weight:600;color:var(--ink)}
.section-title em{font-style:normal;color:var(--orange)}
.services .lead{position:absolute;left:0;top:127px;width:1200px;text-align:center;font-size:13px;line-height:19px}
.case{position:absolute;top:199px;width:320px;height:374px;background:var(--white)}
.case-icon{position:absolute;left:22px;top:38px;width:56px;height:56px;border-radius:50%;background:var(--orange);box-shadow:0 0 0 4px #fff,0 0 0 6px var(--orange)}
.case h3{position:absolute;left:101px;top:36px;font-size:20px;font-weight:500;color:var(--ink)}
.case p{position:absolute;left:101px;top:75px;width:200px;font-size:13px;line-height:19px}
.read{position:absolute;font-size:13px;color:#333;display:flex;align-items:center;gap:8px}
.case .read{left:101px;top:124px}
.case-img{position:absolute;left:0;top:178px;width:320px;height:196px}

/* blog */
.blog{position:absolute;top:2017px;left:0;width:1200px;height:808px}
.post{position:absolute;top:158px;width:320px;height:449px;border:1px solid var(--line);background:var(--white)}
.post-img{position:absolute;left:-1px;top:-1px;width:320px;height:239px}
.meta{position:absolute;left:24px;top:262px;font-size:13px;display:flex;gap:22px}
.post h3{position:absolute;left:24px;top:296px;width:280px;font-size:19px;line-height:21px;font-weight:600;color:var(--ink)}
.post p{position:absolute;left:24px;top:357px;width:270px;font-size:13px;line-height:20px}
.post .read{left:24px;top:411px}
.pager{position:absolute;left:567px;top:2664px;display:flex;gap:6px;align-items:center}
.pager i{width:12px;height:12px;border:2px solid var(--orange);border-radius:50%;display:block}
.pager i.on{width:14px;height:14px;background:var(--orange)}

/* footer */
.footer{position:absolute;top:2825px;left:0;width:1200px;height:461px;background:linear-gradient(180deg,var(--navy),var(--navy-deep))}
.cta{position:absolute;left:96px;top:2745px;width:1007px;height:175px;border-radius:45px;background:var(--cta-grey)}
.cta h2{position:absolute;left:78px;top:68px;font-size:25px;line-height:30px;color:var(--white);font-weight:600}
.cta .btn{position:absolute;left:767px;top:56px;width:193px;height:62px;background:var(--navy);font-size:14px;font-weight:400}
.flogo{position:absolute;left:104px;top:148px;color:var(--white);font-family:"Poppins",sans-serif;font-size:38px;font-weight:400;line-height:1}
.flogo small{display:block;font-size:12px;letter-spacing:6px;padding-left:34px;margin-top:4px}
.fabout{position:absolute;left:96px;top:232px;width:240px;font-size:13px;line-height:22px;color:#e4e7ee}
.fsocial-label{position:absolute;left:96px;top:319px;color:var(--white);font-family:"Poppins",sans-serif;font-size:14px;font-weight:500}
.footer .social{position:absolute;left:96px;top:356px}
.footer .social span{border-color:#aab}
.footer h4{position:absolute;top:160px;font-size:20px;font-weight:500;color:var(--white)}
.flinks{position:absolute;top:208px;display:grid;grid-template-columns:101px 100px;row-gap:9px;font-size:13px;color:#eef}
.recent{position:absolute;left:650px;width:180px;display:flex;gap:16px}
.recent .thumb{width:56px;height:56px;flex:none;background:linear-gradient(135deg,#a9c4f0,#e7739a)}
.recent b{display:block;font-size:11px;font-weight:600;color:#eef;line-height:14px}
.recent small{display:flex;gap:6px;font-size:10px;color:#eef;margin-top:2px}
.hours{position:absolute;left:893px;top:202px;width:210px;list-style:none;font-size:13px;color:#eef}
.hours li{display:flex;justify-content:space-between;height:34px;padding-top:8px;border-bottom:1px solid #56607a}
.copyright{position:absolute;left:0;top:3233px;width:1200px;height:53px;background:var(--orange);clip-path:polygon(56px 0,1144px 0,1200px 100%,0 100%);color:#fff;font-size:13px;text-align:center;line-height:53px}
</style>
</head>
<body>

<div class="topbar">
  <div class="social"><span></span><span></span><span></span><span></span></div>
  <div class="toplinks"><a>Blog</a><a>About Us</a><a>Contact Us</a><a>01632960000</a></div>
</div>

<header class="header">
  <div class="logo">vanta<small>DIGITAL</small></div>
  <nav class="nav"><a>Create</a><a>Communicate</a><a>Convert</a><a>Close</a><a>Case Studies</a></nav>
  <div class="search"></div>
  <a class="btn">LEARN MORE <span>+</span></a>
</header>

<section class="hero">
  <div class="deco" role="img" aria-label="Grey dotted decoration" style="left:96px;top:45px;width:120px;height:120px;background:radial-gradient(circle,rgba(190,190,190,.35),rgba(190,190,190,0) 70%)"></div>
  <div class="hero-badge"></div>
  <div class="hero-tags">• Create &nbsp;• Communicate &nbsp;• Convert &nbsp;• Close</div>
  <h1>Growth works<br>for you</h1>
  <p>Today, Marlow's is on the cusp of continued global expansion with over 100,000 members working out w eekly in studios</p>
  <a class="btn">SET UP A CALL <span>+</span></a>
  <div class="deco" role="img" aria-label="Orange dotted decoration" style="left:450px;top:500px;width:125px;height:125px;background:radial-gradient(circle,rgba(240,100,31,.22),rgba(240,100,31,0) 70%)"></div>
  <div class="hero-art" role="img" aria-label="Illustration of a team climbing a growth arrow beside a large phone showing a web page"></div>
</section>

<section class="intro">
  <div class="intro-art-a" role="img" aria-label="Illustration of a hand holding a phone with a megaphone"></div>
  <div class="intro-art-b" role="img" aria-label="Illustration of a businessman walking up a rising purple arrow"></div>
  <div class="intro-pill">Vanta: Where Growth Works</div>
  <div class="intro-lines"></div>
  <div class="intro-watermark"></div>
  <h2>Fed up with agencies who don't care? We've heard that before.</h2>
  <ul class="checks">
    <li><svg width="11" height="9" viewBox="0 0 11 9"><path d="M1 4.5l3 3L10 1" fill="none" stroke="#f0641f" stroke-width="1.6"/></svg>We know every client has unique needs. Yet, few digital agencies spend enough time getting to know the client's business.</li>
    <li><svg width="11" height="9" viewBox="0 0 11 9"><path d="M1 4.5l3 3L10 1" fill="none" stroke="#f0641f" stroke-width="1.6"/></svg>We're different. We take a highly personalised approach to every project, working closely with our clients to understand their objectives, challenges and target audience.</li>
    <li><svg width="11" height="9" viewBox="0 0 11 9"><path d="M1 4.5l3 3L10 1" fill="none" stroke="#f0641f" stroke-width="1.6"/></svg>Knowing your business is the first step in helping you grow. It's how we work, and it will work for you.</li>
  </ul>
  <h3>Achieve growth that works</h3>
  <a class="btn">Set Up A Call</a>
</section>

<section class="services">
  <h2 class="section-title" style="top:78px"><em>Vanta:</em> Where Growth Works</h2>
  <p class="lead">We understand the importane of a strong online presence. That's why we offer a complete range<br>of digital marketing solutions to help you reach your growth goals.</p>
  <article class="case" style="left:96px">
    <div class="case-icon"></div><h3>Case Study 1</h3>
    <p>Knowing your business is the first step in helping you grow.</p>
    <a class="read"><svg width="11" height="10" viewBox="0 0 11 10"><path d="M0 5h9M5 1l4 4-4 4" fill="none" stroke="#333" stroke-width="1.5"/></svg>Read More</a>
    <div class="case-img" role="img" aria-label="Illustration of people climbing green stairs toward a star" style="background:linear-gradient(180deg,#e9c864 0%,#d9b45a 45%,#2f9a7c 70%,#c0563a 100%)"></div>
  </article>
  <article class="case" style="left:440px">
    <div class="case-icon"></div><h3>Case Study 2</h3>
    <p>Knowing your business is the first step in helping you grow.</p>
    <a class="read"><svg width="11" height="10" viewBox="0 0 11 10"><path d="M0 5h9M5 1l4 4-4 4" fill="none" stroke="#333" stroke-width="1.5"/></svg>Read More</a>
    <div class="case-img" role="img" aria-label="Illustration of a woman beside a laptop with online shop icons" style="background:radial-gradient(circle at 55% 50%,#7fa4f2 0,#4a5ec9 45%,#3a49a8 100%)"></div>
  </article>
  <article class="case" style="left:783px">
    <div class="case-icon"></div><h3>Case Study 3</h3>
    <p>Knowing your business is the first step in helping you grow.</p>
    <a class="read"><svg width="11" height="10" viewBox="0 0 11 10"><path d="M0 5h9M5 1l4 4-4 4" fill="none" stroke="#333" stroke-width="1.5"/></svg>Read More</a>
    <div class="case-img" role="img" aria-label="Illustration of two people by a dashboard screen and a target" style="background:linear-gradient(120deg,#e3b6ea,#b9b8f2 45%,#6f8cf0)"></div>
  </article>
</section>

<section class="blog">
  <h2 class="section-title" style="top:75px">From the Blog</h2>
  <article class="post" style="left:96px">
    <div class="post-img" role="img" aria-label="Illustration of people around a giant computer and keyboard" style="background:radial-gradient(circle at 50% 55%,#8f86e0 0,#f3c478 45%,#f7dcae 100%)"></div>
    <div class="meta"><span>By: Admin</span><span>▦ Jan,6, 2023</span></div>
    <h3>Searchly's new PPC features are loaded with AI</h3>
    <p>Knowing your business is the first step in helping you grow.</p>
    <a class="read"><svg width="11" height="10" viewBox="0 0 11 10"><path d="M0 5h9M5 1l4 4-4 4" fill="none" stroke="#333" stroke-width="1.5"/></svg>Read More</a>
  </article>
  <article class="post" style="left:440px">
    <div class="post-img" role="img" aria-label="Illustration of people with charts, a magnifier and a keyboard" style="background:linear-gradient(135deg,#f4eaf2,#e6c9dc 50%,#9fb3d6)"></div>
    <div class="meta"><span>By: Admin</span><span>▦ Jan,6, 2023</span></div>
    <h3>How Searchly Killed the Broad Match Keyword?</h3>
    <p>Knowing your business is the first step in helping you grow.</p>
    <a class="read"><svg width="11" height="10" viewBox="0 0 11 10"><path d="M0 5h9M5 1l4 4-4 4" fill="none" stroke="#333" stroke-width="1.5"/></svg>Read More</a>
  </article>
  <article class="post" style="left:783px">
    <div class="post-img" role="img" aria-label="Illustration of social media icons around a megaphone" style="background:radial-gradient(circle at 55% 50%,#f7c44a 0,#ef6a8a 25%,#8fa6f4 55%,#6a86ee 100%)"></div>
    <div class="meta"><span>By: Admin</span><span>▦ Jan,6, 2023</span></div>
    <h3>The 9 Rules of Social Media Engagement (Part II)</h3>
    <p>Knowing your business is the first step in helping you grow.</p>
    <a class="read"><svg width="11" height="10" viewBox="0 0 11 10"><path d="M0 5h9M5 1l4 4-4 4" fill="none" stroke="#333" stroke-width="1.5"/></svg>Read More</a>
  </article>
</section>
<div class="pager"><i></i><i class="on"></i><i></i><i></i></div>

<footer class="footer">
  <div class="flogo">vanta<small>DIGITAL</small></div>
  <p class="fabout">Our approach to itis unique around know work an we know doesn't work verified factors in play.</p>
  <div class="fsocial-label">Social Media:</div>
  <div class="social"><span></span><span></span><span></span><span></span></div>

  <h4 style="left:385px">Service Links</h4>
  <div class="flinks" style="left:385px"><a>Faq</a><a>Privacy</a><a>Policy</a><a>About</a><a>Support</a><a>Skill</a><a>Team</a><a>Blog</a><a>Projects</a><a>Contact</a></div>

  <h4 style="left:650px">Recent Post</h4>
  <div class="recent" style="top:205px"><div class="thumb" role="img" aria-label="Post thumbnail illustration"></div><div><b>Received shutters expenses.</b><small><span style="color:#f0641f">▦</span>Jun,5,2023</small></div></div>
  <div class="recent" style="top:269px"><div class="thumb" role="img" aria-label="Post thumbnail illustration"></div><div><b>Received shutters expenses.</b><small><span style="color:#f0641f">▦</span>Jun,5,2023</small></div></div>

  <h4 style="left:893px">Open Time</h4>
  <ul class="hours">
    <li><span>Friday</span><span>9AM–9PM</span></li>
    <li><span>Saturday</span><span>9AM–9PM</span></li>
    <li><span>Sunday</span><span>9AM–8PM</span></li>
    <li><span>Monday</span><span>9AM–8PM</span></li>
    <li><span>Tuesday</span><span>9AM–8PM</span></li>
  </ul>
</footer>

<div class="cta">
  <h2>We're the turbo boost for your<br>digital marketing engine.</h2>
  <a class="btn">Put Your Foot Down</a>
</div>

<div class="copyright">Copyright © 2023 Vanta Digital Limited, All Rights Reserved.</div>

</body>
</html>
```